Safety Training company business card design

We are after a high quality, professional business card. We are open to a single or double sided card.

The winning designer must provide the card in a format where we can easily change the name and details of the different people in our organization.

Harbor Guard's company colour is lime green.

We provide all aspects of safety advisory and training for the Building, Civil Construction, Mining, Oil and Gas, Manufacturing, Rail, Rural and Retail sectors.

Visit our website www.harborguard.com.au for training competencies we offer along with our other services including RPL's, safety audits, professional development and client support.

Target Market(s)

Those in the Building, Civil Construction, Mining, Oil and Gas, Manufacturing, Rail, Rural and Retail industries.

Industry/Entity Type

Training

Contact Information for Business Card

Harbor Guard
Safety and Training
Dennis Palworth
Director
M 0427 518 266
dennis@harborguard.com.au
www.harborguard.com.au
(2 business addresses:)
Corvin High Risk Training Centre
17 Tandem Parade, Corvin Q 4215 P 3912 5486 F 3912 5174
Brenlow Training Centre
86 Fenwick Street, Brenlow Q 4781 P 4873 2615 F 4873 2249

Colors
9bcb3c

Requirements
Must have
• Lime green must be the main colour. must include HG logo attached, and state Harbor Guard (Safety and Training in smaller/different font).

State something along the lines of:

Nice to have
• We offer remote training and we can come to you.

```html
<!DOCTYPE html>
<html lang="en">
<head>
<meta charset="utf-8">
<title>Harbor Guard – Business Card</title>
<link rel="stylesheet" href="https://fonts.googleapis.com/css2?family=Exo+2:wght@300;400;600&display=swap">
<style>
:root{
  --lime:#9bcb3c;
  --ink:#1c1c1c;
  --white:#ffffff;
  --page:#ffffff;
}
*{margin:0;padding:0;box-sizing:border-box}
html,body{width:959px;height:1200px;overflow:hidden;background:var(--page)}
body{position:relative;font-family:"Exo 2",sans-serif;color:var(--white)}
.card{position:absolute;left:55px;width:848px;height:531px;background:var(--ink);overflow:hidden}
.card--front{top:47px}
.card--back{top:618px}
.card__shapes{position:absolute;inset:0;width:848px;height:531px}
.card__shapes polygon{fill:var(--lime)}

.brand-mark{position:absolute;left:68px;top:62px;font-weight:600;font-size:112px;line-height:1;color:var(--lime);letter-spacing:2px}
.brand-name{position:absolute;left:34px;top:352px;font-weight:600;font-size:55px;letter-spacing:3px;line-height:1;white-space:nowrap}
.brand-name__accent{color:var(--lime)}
.brand-url{position:absolute;left:35px;top:412px;font-weight:400;font-size:28px;letter-spacing:2px;line-height:1}
.brand-rule{position:absolute;left:0;top:466px;width:445px;height:4px;background:var(--lime)}
.brand-about{position:absolute;left:6px;top:484px;width:660px;font-weight:300;font-size:14.5px;letter-spacing:1px;line-height:19px;white-space:nowrap}

.contact{position:absolute;right:66px;text-align:right;font-weight:300;font-size:23px;letter-spacing:1.6px;line-height:28px;white-space:nowrap}
.contact--brenlow{top:16px}
.contact--corvin{top:95px}
.contact--mobile{top:205px}
.contact--email{top:256px}
.contact--web{top:308px}
.icon{position:absolute;left:810px;width:24px;height:24px}
.icon path,.icon circle,.icon rect,.icon line{fill:none;stroke:var(--white);stroke-width:1.6}
.icon .solid{fill:var(--white);stroke:none}

.person-rule{position:absolute;left:563px;top:375px;width:285px;height:4px;background:var(--lime)}
.person-name{position:absolute;right:23px;top:398px;font-weight:600;font-size:44px;letter-spacing:2px;line-height:1;white-space:nowrap}
.person-name__last{color:var(--lime)}
.person-role{position:absolute;right:23px;top:458px;font-weight:400;font-size:18px;letter-spacing:1.5px}
</style>
</head>
<body>

<section class="card card--front">
  <svg class="card__shapes" viewBox="0 0 848 531" aria-hidden="true">
    <polygon points="382,0 848,0 848,114 500,232"/>
    <polygon points="515,257 848,145 848,531 653,531"/>
  </svg>
  <div class="brand-mark">HG</div>
  <h1 class="brand-name">HARBOR <span class="brand-name__accent">GUARD</span></h1>
  <p class="brand-url">www.harborguard.com.au</p>
  <div class="brand-rule"></div>
  <p class="brand-about">We provide all aspects of safety advisory and training for the Building, Civil Con-<br>struction, Mining, Oil and Gas, Manufacturing, Rail, Rural and Retail sectors.</p>
</section>

<section class="card card--back">
  <svg class="card__shapes" viewBox="0 0 848 531" aria-hidden="true">
    <polygon points="0,0 196,0 332,272 0,385"/>
    <polygon points="0,415 348,297 466,531 0,531"/>
  </svg>

  <p class="contact contact--brenlow">Brenlow Training Centre 86 Fenwick Street,<br>Brenlow Q 4781 P 4873 2615 F 4873 2249</p>
  <svg class="icon" style="top:32px" viewBox="0 0 24 24" aria-hidden="true"><path d="M12 22 L7 11 A6 6 0 1 1 17 11 Z"/><circle cx="12" cy="8" r="2.4"/></svg>

  <p class="contact contact--corvin">Corvin High Risk Training Centre 17<br>Tandem Parade, Corvin Q 4215<br>P 3912 5486 F 3912 5174</p>
  <svg class="icon" style="top:124px" viewBox="0 0 24 24" aria-hidden="true"><path d="M12 22 L7 11 A6 6 0 1 1 17 11 Z"/><circle cx="12" cy="8" r="2.4"/></svg>

  <p class="contact contact--mobile">0427 518 266</p>
  <svg class="icon" style="top:208px;width:28px;height:28px;left:808px" viewBox="0 0 28 28" aria-hidden="true"><rect class="solid" x="0" y="0" width="28" height="28" rx="4"/><path d="M10 6 L13 6 L13 10 L11 11 Q12 16 15 19 L17 17 L21 19 L20 22 Q12 22 9 12 Z" style="fill:var(--ink);stroke:none"/></svg>

  <p class="contact contact--email">dennis@harborguard.com.au</p>
  <svg class="icon" style="top:262px;width:28px;left:808px" viewBox="0 0 28 24" aria-hidden="true"><rect x="1" y="3" width="26" height="18"/><path d="M1 3 L14 14 L27 3 M1 21 L11 11 M27 21 L17 11"/></svg>

  <p class="contact contact--web">www.harborguard.com.au</p>
  <svg class="icon" style="top:314px" viewBox="0 0 24 24" aria-hidden="true"><circle cx="12" cy="12" r="10.5"/><path d="M12 1.5 C6 6 6 18 12 22.5 C18 18 18 6 12 1.5 M1.5 12 H22.5 M3 7 H21 M3 17 H21"/></svg>

  <div class="person-rule"></div>
  <h2 class="person-name">Dennis <span class="person-name__last">Palworth</span></h2>
  <p class="person-role">Director</p>
</section>

</body>
</html>
```